Business Card Design for digital storytelling business

I need a business card for a workshop/consulting/coaching business.

Company Name: Bright Harbor Works

Tagline: New ways to share the stories of a life

What we do: Through workshops, webinars, and coaching we teach you how to capture, tell and share your important memories and stories using readily available digital tools. We will help you tell your life story in a format to share with your family now and in the future.
Updates

I just received a toll free number that I would like included on the designs. If the addition of a phone number would significantly alter your design, please submit an altered version. The number is 866-217-9086

Target Market(s)

Adults in US between ages of 35-70 interested in capturing, preserving and sharing memories and life stories in a digital format.
Could include the following:

-People touched by illness or tragedy who need to tell their own or a loved one's life story
-Grandparents wanting to share stories and wisdom with grandchildren living far away
-People with aging parents who want to capture their stories in a format to pass on to their children
-Alzheimer's patients and their families
-People wanting to transfer analog photos to digital; or wanting to organize digital photos into something that tells a story

Industry/Entity Type

Digital

Requirements
Must have
• Must include business name, logo, tagline

Contact information (see file)
Social media information

Fonts easily readable by aging eyes. Good contrast.

Nice to have
• Color preferences: blue, green, yellow/gold
Blue denotes the calm, non-pressured way that I teach. It is for the healing that comes from telling your story. It represents time and space that are bridged in the digital environment.
Green is for growth, the future, the family tree, Vines that grow and branch and connect the generations and our hearts.
Yellow/gold is for the legacy of wisdom in our lives and stories. It is for the light of truth we bring to the world by sharing our stories.
Should not have
• No old-style, script fonts.
No Times New Roman

```html
<!DOCTYPE html>
<html lang="en">
<head>
<meta charset="utf-8">
<title>Bright Harbor Works – Business Card</title>
<link rel="stylesheet" href="https://fonts.googleapis.com/css2?family=Ubuntu:wght@400;500&family=Exo+2:wght@400;500;600&display=swap">
<style>
  :root {
    --navy: #33426b;
    --green: #219b4a;
    --green-dark: #1b7a3a;
    --cream: #f0dba8;
    --ink: #2b2b2b;
    --white: #ffffff;
    --stage: #e6e6e4;
  }
  * { box-sizing: border-box; margin: 0; padding: 0; }
  html, body { width: 1200px; height: 869px; overflow: hidden; }
  body {
    background: var(--stage);
    font-family: "Exo 2", sans-serif;
    display: flex;
    flex-direction: column;
    align-items: center;
    justify-content: center;
    gap: 40px;
  }
  .card {
    position: relative;
    width: 640px;
    height: 366px;
    overflow: hidden;
    box-shadow: 0 6px 18px rgba(0,0,0,.18);
  }

  /* Back side */
  .card--back { background: var(--navy); }
  .back-brand {
    position: absolute;
    left: 0; right: 0; top: 140px;
    text-align: center;
    color: var(--white);
  }
  .back-brand .brand-name {
    font-family: "Ubuntu", sans-serif;
    font-weight: 500;
    font-size: 38px;
    display: inline-flex;
    align-items: center;
    gap: 14px;
  }
  .back-brand .brand-mark {
    width: 30px; height: 30px;
    background: var(--white);
  }
  .back-brand .tagline {
    font-family: "Ubuntu", sans-serif;
    font-size: 13.5px;
    letter-spacing: 1px;
    text-transform: uppercase;
    margin-top: 6px;
  }

  /* Front side */
  .card--front { background: var(--cream); }
  .front-shapes { position: absolute; inset: 0; }
  .front-brand {
    position: absolute;
    left: 40px; top: 38px;
    color: var(--navy);
  }
  .front-brand .brand-name {
    font-family: "Ubuntu", sans-serif;
    font-weight: 500;
    font-size: 30px;
    display: flex;
    align-items: center;
    gap: 12px;
  }
  .front-brand .brand-mark {
    width: 24px; height: 24px;
    background: var(--navy);
  }
  .front-brand .tagline {
    font-family: "Ubuntu", sans-serif;
    font-size: 11px;
    letter-spacing: .8px;
    text-transform: uppercase;
    margin-top: 4px;
    padding-left: 36px;
  }
  .person {
    position: absolute;
    right: 34px; top: 92px;
    text-align: right;
    color: var(--ink);
  }
  .person .person-name {
    font-size: 22px;
    font-weight: 600;
    letter-spacing: 1.5px;
  }
  .person .person-role {
    font-size: 11px;
    letter-spacing: 1px;
    text-transform: uppercase;
  }
  .address {
    position: absolute;
    left: 118px; top: 146px;
    color: var(--white);
    font-size: 14px;
    font-weight: 500;
    letter-spacing: .5px;
  }
  .contact-list {
    position: absolute;
    list-style: none;
    color: var(--white);
    font-size: 14px;
    letter-spacing: .6px;
  }
  .contact-list li {
    display: flex;
    align-items: center;
    gap: 12px;
    margin-bottom: 10px;
  }
  .contact-list--web { left: 34px; top: 196px; }
  .contact-list--phone { right: 40px; top: 226px; }
  .icon {
    width: 24px; height: 24px;
    background: var(--white);
    border-radius: 3px;
    display: flex;
    align-items: center;
    justify-content: center;
    flex: none;
  }
  .icon svg { width: 16px; height: 16px; }
</style>
</head>
<body>

  <section class="card card--back" aria-label="Business card back">
    <div class="back-brand">
      <div class="brand-name"><span class="brand-mark"></span>Bright Harbor Works</div>
      <div class="tagline">New ways to share the stories of a life</div>
    </div>
  </section>

  <section class="card card--front" aria-label="Business card front">
    <svg class="front-shapes" viewBox="0 0 640 366" width="640" height="366" aria-hidden="true">
      <polygon points="0,176 640,176 640,366 0,366" fill="var(--navy)"/>
      <polygon points="0,300 640,322 640,366 0,366" fill="var(--green)"/>
      <polygon points="82,138 560,138 590,164 560,176 82,176" fill="var(--green)"/>
      <polygon points="560,176 590,164 600,196" fill="var(--green-dark)"/>
      <polygon points="66,146 82,138 82,152" fill="var(--navy)"/>
    </svg>

    <div class="front-brand">
      <div class="brand-name"><span class="brand-mark"></span>Bright Harbor Works</div>
      <div class="tagline">New ways to share the stories of a life</div>
    </div>

    <div class="person">
      <div class="person-name">DANA WHITFIELD</div>
      <div class="person-role">General Manager</div>
    </div>

    <div class="address">214, 6th floor, Harbor Point Road MLB</div>

    <ul class="contact-list contact-list--web">
      <li>
        <span class="icon">
          <svg viewBox="0 0 16 16"><circle cx="8" cy="8" r="6.5" fill="none" stroke="#33426b" stroke-width="1.4"/><ellipse cx="8" cy="8" rx="2.8" ry="6.5" fill="none" stroke="#33426b" stroke-width="1.2"/><line x1="1.5" y1="8" x2="14.5" y2="8" stroke="#33426b" stroke-width="1.2"/></svg>
        </span>
        www.brightharborworks.com
      </li>
      <li>
        <span class="icon">
          <svg viewBox="0 0 16 16"><rect x="1.5" y="3.5" width="13" height="9" fill="none" stroke="#33426b" stroke-width="1.4"/><polyline points="1.5,3.5 8,9 14.5,3.5" fill="none" stroke="#33426b" stroke-width="1.4"/></svg>
        </span>
        hello@brightharbor.com
      </li>
    </ul>

    <ul class="contact-list contact-list--phone">
      <li>
        <span class="icon">
          <svg viewBox="0 0 16 16"><path d="M4 2 L6.5 2 L7.5 5 L6 6.2 C6.8 8 8 9.2 9.8 10 L11 8.5 L14 9.5 L14 12 C14 13 13 14 12 14 C7 13.5 2.5 9 2 4 C2 3 3 2 4 2 Z" fill="#33426b"/></svg>
        </span>
        866-217-9086
      </li>
      <li>
        <span class="icon">
          <svg viewBox="0 0 16 16"><rect x="4" y="1.5" width="8" height="13" rx="1.5" fill="#33426b"/><rect x="5.3" y="3" width="5.4" height="8.5" fill="#fff"/><circle cx="8" cy="13" r=".8" fill="#fff"/></svg>
        </span>
        866-217-4410
      </li>
    </ul>
  </section>

</body>
</html>
```